Kestrel Fitness Studio Retail Tube Design

We require a design for cardboard tubes, like images included, which will be the main packaging for the clothing sold in our fitness studio. Kestrel Fitness Studio is an upscale customer service driven fitness studio that is geared towards improving our clients/members quality of life by marrying cutting edge technology like 3D scanning and metabolic measurement with first class training based on 30+ years of experience in the industry.

The project will require a design which revolves around the tube seamlessly including the lid and its top and must include the company logo, which is included, along with our web address (www.kestrelgymhall.example).

The final design should be a bold, sleek design which stands out so when people see the tube they will either know it’s from our studio or be curious as to want company it’s from. Similar to the impact the Moravanti bag has that is given to all their customers.

Target Market(s)

Individuals and groups seeking individualize fitness programs which produce results.

Industry/Entity Type

Clothing

Colors

Designer to choose colors to be used in the design.

Requirements
Must have
• Logo and website address

```html
<!DOCTYPE html>
<html lang="en">
<head>
<meta charset="utf-8">
<title>Kestrel Fitness Studio – Retail Tube Designs</title>
<link href="https://fonts.googleapis.com/css2?family=Questrial&display=swap" rel="stylesheet">
<style>
  :root {
    --canvas: #ffffff;
    --red: #d71f30;
    --black: #1f1f1f;
    --charcoal: #3b3b3d;
    --charcoal-top: #2a2a2b;
    --silver: #c4c4c4;
    --kraft: #cdb08a;
    --kraft-top: #3a3430;
    --paper: #f4f4f4;
    --paper-top: #e6e6e6;
    --white: #ffffff;
  }
  html, body {
    margin: 0;
    padding: 0;
    width: 1200px;
    height: 1112px;
    overflow: hidden;
    background: var(--canvas);
  }
  .canvas {
    position: relative;
    width: 1200px;
    height: 1112px;
  }
  .tube {
    position: absolute;
    width: 182px;
    height: 440px;
    overflow: visible;
  }
  .tube--charcoal { left: 264px; top: 186px; }
  .tube--kraft    { left: 744px; top: 186px; }
  .tube--paper    { left: 504px; top: 523px; }

  .tube__body { }
  .tube--charcoal .tube__body { fill: var(--charcoal); }
  .tube--kraft .tube__body    { fill: var(--kraft); }
  .tube--paper .tube__body    { fill: var(--paper); }

  .tube--charcoal .tube__top { fill: var(--charcoal-top); }
  .tube--kraft .tube__top    { fill: var(--kraft-top); }
  .tube--paper .tube__top    { fill: var(--paper-top); }

  .tube__rim { fill: none; stroke-width: 2; }
  .tube--charcoal .tube__rim { stroke: #4a4a4c; }
  .tube--kraft .tube__rim    { stroke: #b89a74; }
  .tube--paper .tube__rim    { stroke: #fafafa; }

  .tube__seam { fill: none; stroke: rgba(0,0,0,0.12); stroke-width: 1; }
  .tube__line { fill: none; stroke: var(--red); stroke-width: 3; }
  .tube__line--silver { stroke: var(--silver); }
  .tube__band--red { fill: var(--red); }
  .tube__band--black { fill: var(--black); }

  .brand__mark { fill: var(--red); }
  .brand__name {
    font-family: "Questrial", sans-serif;
    font-size: 44px;
    letter-spacing: 1px;
    text-anchor: middle;
  }
  .brand__tagline {
    font-family: "Questrial", sans-serif;
    font-size: 9.5px;
    letter-spacing: 1.2px;
    text-anchor: middle;
    text-transform: uppercase;
  }
  .tube--charcoal .brand__name,
  .tube--charcoal .brand__tagline { fill: var(--silver); }
  .tube--kraft .brand__name,
  .tube--kraft .brand__tagline,
  .tube--paper .brand__name,
  .tube--paper .brand__tagline { fill: var(--black); }

  .tube__web {
    font-family: "Questrial", sans-serif;
    font-size: 9px;
    letter-spacing: 0.8px;
    text-anchor: middle;
    fill: var(--white);
  }
</style>
</head>
<body>
<main class="canvas">
  <svg width="0" height="0" style="position:absolute">
    <defs>
      <linearGradient id="cylinder-shade" x1="0" x2="1" y1="0" y2="0">
        <stop offset="0" stop-color="#000" stop-opacity="0.28"/>
        <stop offset="0.18" stop-color="#000" stop-opacity="0.06"/>
        <stop offset="0.42" stop-color="#fff" stop-opacity="0.12"/>
        <stop offset="0.7" stop-color="#000" stop-opacity="0.02"/>
        <stop offset="1" stop-color="#000" stop-opacity="0.3"/>
      </linearGradient>
    </defs>
  </svg>

  <!-- charcoal tube -->
  <svg class="tube tube--charcoal" viewBox="0 0 182 440" role="group" aria-label="Charcoal tube">
    <path class="tube__body" d="M0 12 H182 V428 A91 10 0 0 1 0 428 Z"/>
    <path class="tube__band--red" d="M0 370 A91 10 0 0 0 182 370 V428 A91 10 0 0 1 0 428 Z"/>
    <path class="tube__line tube__line--silver" d="M0 362 A91 10 0 0 0 182 362"/>
    <path class="tube__seam" d="M0 88 A91 10 0 0 0 182 88"/>
    <path class="tube__line" d="M0 93 A91 10 0 0 0 182 93"/>
    <path fill="url(#cylinder-shade)" d="M0 12 H182 V428 A91 10 0 0 1 0 428 Z"/>
    <ellipse class="tube__top" cx="91" cy="12" rx="91" ry="10"/>
    <ellipse class="tube__rim" cx="91" cy="12" rx="89" ry="9"/>
    <rect class="brand__mark" x="76" y="174" width="30" height="30"/>
    <text class="brand__name" x="91" y="264">kestrel</text>
    <text class="brand__tagline" x="91" y="282">Fitness Studio</text>
    <text class="tube__web" x="91" y="410">www.kestrelgymhall.example</text>
  </svg>

  <!-- kraft tube -->
  <svg class="tube tube--kraft" viewBox="0 0 182 440" role="group" aria-label="Kraft tube">
    <path class="tube__body" d="M0 12 H182 V428 A91 10 0 0 1 0 428 Z"/>
    <path class="tube__band--black" d="M0 372 A91 10 0 0 0 182 372 V428 A91 10 0 0 1 0 428 Z"/>
    <path class="tube__line" d="M0 360 A91 10 0 0 0 182 360"/>
    <path class="tube__seam" d="M0 88 A91 10 0 0 0 182 88"/>
    <path class="tube__line" d="M0 93 A91 10 0 0 0 182 93"/>
    <path fill="url(#cylinder-shade)" d="M0 12 H182 V428 A91 10 0 0 1 0 428 Z"/>
    <ellipse class="tube__top" cx="91" cy="12" rx="91" ry="10"/>
    <ellipse class="tube__rim" cx="91" cy="12" rx="89" ry="9"/>
    <rect class="brand__mark" x="76" y="174" width="30" height="30"/>
    <text class="brand__name" x="91" y="264">kestrel</text>
    <text class="brand__tagline" x="91" y="282">Fitness Studio</text>
    <text class="tube__web" x="91" y="412">www.kestrelgymhall.example</text>
  </svg>

  <!-- white tube -->
  <svg class="tube tube--paper" viewBox="0 0 182 440" role="group" aria-label="White tube">
    <path class="tube__body" d="M0 12 H182 V428 A91 10 0 0 1 0 428 Z"/>
    <path class="tube__band--black" d="M0 383 A91 10 0 0 0 182 383 V428 A91 10 0 0 1 0 428 Z"/>
    <path class="tube__line" d="M0 366 A91 10 0 0 0 182 366"/>
    <path class="tube__seam" d="M0 86 A91 10 0 0 0 182 86"/>
    <path class="tube__line" d="M0 91 A91 10 0 0 0 182 91"/>
    <path fill="url(#cylinder-shade)" d="M0 12 H182 V428 A91 10 0 0 1 0 428 Z"/>
    <ellipse class="tube__top" cx="91" cy="12" rx="91" ry="10"/>
    <ellipse class="tube__rim" cx="91" cy="12" rx="89" ry="9"/>
    <rect class="brand__mark" x="76" y="172" width="30" height="30"/>
    <text class="brand__name" x="91" y="262">kestrel</text>
    <text class="brand__tagline" x="91" y="280">Fitness Studio</text>
    <text class="tube__web" x="91" y="418">www.kestrelgymhall.example</text>
  </svg>
</main>
</body>
</html>
```